Business Card/Stationary
General Contractor
Thank You for all of the submissions so far.
I have eliminated those that had too many curved lines. I like any lines to be more perpendicular/parallel. However, I have left a few with curved lines that I like.
I do like the solid colors on the front and or back.
I have not seen any stationary submissions. I need some of those as well, although not as critical as a business card.
Thank You for your submissions. I will comment again in a couple of days.

```html
<!DOCTYPE html>
<html lang="en">
<head>
<meta charset="utf-8">
<title>KorvMint Stationery</title>
<link href="https://fonts.googleapis.com/css2?family=Questrial&display=swap" rel="stylesheet">
<style>
  :root{
    --backdrop:#e4e4e2;
    --paper:#ffffff;
    --brand-blue:#1f5db0;
    --brand-blue-dark:#174a8f;
    --ink:#3b3b3b;
    --ink-soft:#6a6a6a;
    --shadow:rgba(0,0,0,.18);
  }
  *{box-sizing:border-box;margin:0;padding:0}
  html,body{width:1200px;height:799px;overflow:hidden}
  body{background:var(--backdrop);font-family:"Questrial",Arial,sans-serif;color:var(--ink);position:relative}

  .sheet{position:absolute;background:var(--paper);box-shadow:0 3px 10px var(--shadow);overflow:hidden}

  .brand{display:flex;align-items:center;gap:6px}
  .brand-square{background:var(--brand-blue);flex:none}
  .brand-name{color:var(--ink);line-height:1;letter-spacing:.5px}

  .contact{font-size:7px;line-height:1.45;color:var(--ink-soft)}

  .blue-band{position:absolute;left:0;right:0;bottom:0}
  .blue-band svg{display:block;width:100%;height:100%}

  /* Letterhead */
  .letterhead{left:72px;top:67px;width:461px;height:696px}
  .letterhead .brand{position:absolute;left:24px;top:22px}
  .letterhead .brand-square{width:22px;height:22px}
  .letterhead .brand-name{font-size:26px}
  .letterhead .contact{position:absolute;left:303px;top:24px}
  .letterhead .blue-band{height:16px}

  /* Business card front */
  .card-front{left:636px;top:86px;width:221px;height:135px}
  .card-front .brand{position:absolute;left:14px;top:16px;gap:4px}
  .card-front .brand-square{width:14px;height:14px}
  .card-front .brand-name{font-size:16px}
  .card-front .holder{position:absolute;left:14px;top:62px;font-size:7px;line-height:1.4}
  .card-front .holder strong{font-weight:400;color:var(--ink);display:block;font-size:8px}
  .card-front .contact{position:absolute;left:98px;top:62px;font-size:6px}
  .card-front .blue-band{height:9px}

  /* Business card back */
  .card-back{left:869px;top:86px;width:218px;height:135px;background:var(--brand-blue)}
  .card-back .brand{position:absolute;left:50%;top:22px;transform:translateX(-50%);gap:4px}
  .card-back .brand-square{width:12px;height:12px;background:#fff}
  .card-back .brand-name{font-size:14px;color:#fff}
  .card-back .services{position:absolute;left:0;right:0;top:64px;text-align:center;color:#fff;font-size:6.5px;line-height:1.55;list-style:none}

  /* Envelope front */
  .envelope-front{left:593px;top:396px;width:516px;height:120px;z-index:2}
  .envelope-front .brand{position:absolute;left:22px;top:20px}
  .envelope-front .brand-square{width:18px;height:18px}
  .envelope-front .brand-name{font-size:21px}
  .envelope-front .contact{position:absolute;left:412px;top:18px;font-size:6.5px}
  .envelope-front .blue-band{height:12px}

  /* Envelope back */
  .envelope-back{left:593px;top:508px;width:516px;height:260px;z-index:1}
  .envelope-back .flap{position:absolute;left:0;top:0;width:100%;height:96px}
  .envelope-back .flap svg{display:block;width:100%;height:100%}
  .envelope-back .brand{position:absolute;left:50%;bottom:40px;transform:translateX(-50%)}
  .envelope-back .brand-square{width:18px;height:18px}
  .envelope-back .brand-name{font-size:21px}
</style>
</head>
<body>

  <section class="sheet letterhead" aria-label="Letterhead">
    <div class="brand"><span class="brand-square"></span><span class="brand-name">KorvMint</span></div>
    <address class="contact">
      120 Harbor Lane<br>Suite 4<br>Lakeview, FL 30000<br><br>
      Phone&nbsp;&nbsp;555-010-2040<br>
      Cell&nbsp;&nbsp;&nbsp;&nbsp;&nbsp;&nbsp;555-010-2041<br>
      Fax&nbsp;&nbsp;&nbsp;&nbsp;&nbsp;&nbsp;&nbsp;555-010-2042<br>
      Email&nbsp;&nbsp;&nbsp;dara@korvmint.com
    </address>
    <div class="blue-band">
      <svg viewBox="0 0 461 16" preserveAspectRatio="none"><path d="M0 10 H300 Q320 10 330 4 Q338 0 350 0 H461 V16 H0 Z" fill="var(--brand-blue)"/></svg>
    </div>
  </section>

  <section class="sheet card-front" aria-label="Business card front">
    <div class="brand"><span class="brand-square"></span><span class="brand-name">KorvMint</span></div>
    <div class="holder"><strong>Dara Lenz</strong>President</div>
    <address class="contact">
      120 Harbor Lane, Suite 4<br>Lakeview, FL 30000<br><br>
      Phone 555-010-2040<br>Cell 555-010-2041<br>Fax 555-010-2042<br>dara@korvmint.com
    </address>
    <div class="blue-band">
      <svg viewBox="0 0 221 9" preserveAspectRatio="none"><path d="M0 5 H140 Q150 5 156 2 Q160 0 166 0 H221 V9 H0 Z" fill="var(--brand-blue)"/></svg>
    </div>
  </section>

  <section class="sheet card-back" aria-label="Business card back">
    <div class="brand"><span class="brand-square"></span><span class="brand-name">KorvMint</span></div>
    <ul class="services">
      <li>General Contractor</li>
      <li>Residential &amp; Commercial</li>
      <li>Licensed and Insured</li>
      <li>Free Estimates</li>
    </ul>
  </section>

  <section class="sheet envelope-front" aria-label="Envelope front">
    <div class="brand"><span class="brand-square"></span><span class="brand-name">KorvMint</span></div>
    <address class="contact">
      120 Harbor Lane<br>Suite 4<br>Lakeview, FL 30000<br><br>
      Phone 555-010-2040<br>Cell&nbsp;&nbsp;&nbsp;&nbsp; 555-010-2041<br>Fax&nbsp;&nbsp;&nbsp;&nbsp;&nbsp; 555-010-2042<br>dara@korvmint.com
    </address>
    <div class="blue-band">
      <svg viewBox="0 0 516 12" preserveAspectRatio="none"><path d="M0 7 H330 Q350 7 360 3 Q367 0 380 0 H516 V12 H0 Z" fill="var(--brand-blue)"/></svg>
    </div>
  </section>

  <section class="sheet envelope-back" aria-label="Envelope back">
    <div class="flap">
      <svg viewBox="0 0 516 96" preserveAspectRatio="none">
        <path d="M0 0 H516 V18 Q516 26 506 30 L272 90 Q258 94 244 90 L10 30 Q0 26 0 18 Z" fill="var(--brand-blue)"/>
        <path d="M0 8 H516" stroke="var(--brand-blue-dark)" stroke-width="2"/>
      </svg>
    </div>
    <div class="brand"><span class="brand-square"></span><span class="brand-name">KorvMint</span></div>
  </section>

</body>
</html>
```